Professional & attention grabbing.

A business card design, front and back. I already have a logo I will attach, but I am open to something new as well.
Things to include:
Name:
Title:
Phone:
Email:
Wanting something that is professional but attention grabbing.
Also we do a lot of work using drones on natural gas pipelines (leading the future)if you want to include any of that. I'm open to ideas.
Target Market(s)
Natural gas transmission industry / greenhouse gas mitigation industry
Industry/Entity Type
Business
Contact Information for Business Card
All details have been conveyed above.
Colors
Designer to choose colors to be used in the design.
Look and feel
Each slider illustrates characteristics of the customer's brand and the style your logo design should communicate.

```html
<!DOCTYPE html>
<html lang="en">
<head>
<meta charset="utf-8">
<title>Vantor Field Inspections – Business Card</title>
<link rel="stylesheet" href="https://fonts.googleapis.com/css2?family=Open+Sans:ital,wght@0,400;0,600;0,700;1,400&display=swap">
<style>
  :root {
    --bg: #e6e6e6;
    --card-white: #ffffff;
    --charcoal: #363638;
    --red: #c01f25;
    --text-grey: #4a4a4c;
    --rule: #8c8c8c;
    --tint: #f8eeee;
  }
  * { margin: 0; padding: 0; box-sizing: border-box; }
  html, body {
    width: 1200px; height: 987px; overflow: hidden;
    background: var(--bg);
    font-family: "Open Sans", Arial, sans-serif;
  }
  .canvas { position: relative; width: 1200px; height: 987px; }

  .card {
    position: absolute; left: 293px; width: 615px; height: 352px;
    overflow: hidden;
  }
  .card--front { top: 130px; background: var(--card-white); }
  .card--back  { top: 505px; background: var(--charcoal); }

  .front__tint {
    position: absolute; left: 0; top: 0; width: 328px; height: 250px;
    background: linear-gradient(160deg, var(--tint) 0%, #fbf6f6 55%, rgba(255,255,255,0) 100%);
  }

  .brand {
    position: absolute; display: flex; align-items: center; gap: 10px;
  }
  .brand__square { width: 22px; height: 22px; background: var(--red); flex: none; }
  .brand__name {
    font-weight: 700; text-transform: uppercase; line-height: 1.05;
  }
  .brand--front { right: 32px; top: 42px; }
  .brand--front .brand__name { color: var(--charcoal); font-size: 19px; width: 168px; }

  .brand--back {
    left: 0; right: 0; top: 118px; justify-content: center; gap: 14px;
  }
  .brand--back .brand__square { width: 34px; height: 34px; }
  .brand--back .brand__name { color: #fff; font-size: 30px; letter-spacing: 1px; }

  .person { position: absolute; left: 32px; top: 183px; }
  .person__name {
    color: var(--red); font-size: 21px; font-weight: 600; line-height: 1.1; text-transform: uppercase;
  }
  .person__title { color: var(--text-grey); font-size: 16px; line-height: 1.4; text-transform: uppercase; }

  .rule {
    position: absolute; left: 32px; top: 237px; width: 552px; height: 1px; background: var(--rule);
  }

  .contacts { position: absolute; left: 32px; top: 245px; list-style: none; }
  .contacts li {
    display: flex; align-items: center; gap: 8px;
    color: var(--text-grey); font-size: 16px; height: 24px;
  }
  .contacts svg { width: 14px; height: 14px; fill: var(--red); flex: none; }

  .front__band { position: absolute; left: 0; bottom: 0; width: 615px; height: 13px; }

  .back__web {
    position: absolute; left: 0; right: 0; top: 300px; text-align: center;
    color: #fff; font-size: 16px; font-style: italic; letter-spacing: 4px;
  }
</style>
</head>
<body>
<main class="canvas">
  <section class="card card--front" aria-label="Business card front">
    <div class="front__tint"></div>
    <div class="brand brand--front">
      <span class="brand__square"></span>
      <span class="brand__name">Vantor Field Inspections</span>
    </div>
    <div class="person">
      <p class="person__name">Daniel Reyes</p>
      <p class="person__title">CEO/Founder</p>
    </div>
    <div class="rule"></div>
    <ul class="contacts">
      <li>
        <svg viewBox="0 0 24 24"><path d="M6.6 10.8a15.1 15.1 0 0 0 6.6 6.6l2.2-2.2a1 1 0 0 1 1-.25 11.4 11.4 0 0 0 3.6.57 1 1 0 0 1 1 1V20a1 1 0 0 1-1 1A17 17 0 0 1 3 4a1 1 0 0 1 1-1h3.5a1 1 0 0 1 1 1c0 1.25.2 2.45.57 3.57a1 1 0 0 1-.25 1z"/></svg>
        555 014 2290
      </li>
      <li>
        <svg viewBox="0 0 24 24"><path d="M2 5h20v14H2z M3 6l9 7 9-7" fill="var(--red)"/><path d="M3.5 6.5 12 12.5l8.5-6" fill="none" stroke="#fff" stroke-width="1.6"/></svg>
        daniel@vantorfield.com
      </li>
      <li>
        <svg viewBox="0 0 24 24"><circle cx="12" cy="12" r="10"/><path d="M2 12h20M12 2c3 3 3 17 0 20M12 2c-3 3-3 17 0 20" fill="none" stroke="#fff" stroke-width="1.4"/></svg>
        www.vantorfield.com
      </li>
    </ul>
    <svg class="front__band" viewBox="0 0 615 13" preserveAspectRatio="none">
      <polygon points="0,0 404,0 400,13 0,13" fill="var(--red)"/>
      <polygon points="408,0 615,0 615,13 404,13" fill="var(--charcoal)"/>
    </svg>
  </section>

  <section class="card card--back" aria-label="Business card back">
    <div class="brand brand--back">
      <span class="brand__square"></span>
      <span class="brand__name">Vantor Field Inspections</span>
    </div>
    <p class="back__web">www.vantorfield.com</p>
  </section>
</main>
</body>
</html>
```